Pediatric Pelvic Health Brochure

Looking to design a brochure for Marlow Crest's pelvic health program. I can provide imagery once I see the layout. Our website is marlowcrestpt.example so the look should reflect that

If you see PDF titled blue and word doc you will see what we provided as thoguhts.

Target Market(s)

parents of children

Industry/Entity Type

Health And Wellness

Font styles to use
Serif

Requirements
Must have
• clear call outs - easy to read with copy,
Should not have
• not look bland or dated

```html
<!DOCTYPE html>
<html lang="en">
<head>
<meta charset="utf-8">
<title>Marlow Crest – Pediatric Pelvic Health Brochure</title>
<link rel="stylesheet" href="https://fonts.googleapis.com/css2?family=Lato:wght@400;700&family=Montserrat:wght@700;800&family=Libre+Baskerville&display=swap">
<style>
:root{
  --navy:#1c3faa;
  --navy-deep:#142f8c;
  --cyan:#1fb2e6;
  --cyan-soft:#2cc2f0;
  --white:#ffffff;
  --page:#e8e9ed;
  --ink-blue:#1c3faa;
}
*{box-sizing:border-box;margin:0;padding:0}
html,body{width:728px;height:1200px;overflow:hidden;background:var(--page)}
body{font-family:"Lato",sans-serif;position:relative}
.sheet{position:absolute;left:14px;width:700px;height:570px;display:grid;grid-template-columns:repeat(3,1fr);box-shadow:0 4px 14px rgba(0,0,0,.18)}
.sheet--outside{top:14px}
.sheet--inside{top:614px;background:var(--navy);padding:8px;gap:8px}
.panel{position:relative;overflow:hidden;min-width:0}
.photo{background:linear-gradient(135deg,#cfe6f3,#8fc7e6 55%,#e9eef3)}
.heading{font-family:"Montserrat",sans-serif;font-weight:800;letter-spacing:1.5px;text-transform:uppercase}

/* outside: diagnoses */
.panel--diagnoses{background:var(--white);padding:22px 18px 0}
.panel--diagnoses .heading{color:var(--navy);font-size:14px;letter-spacing:1px;line-height:1.25;text-align:center;position:relative;padding:0 22px}
.panel--diagnoses .heading::before,.panel--diagnoses .heading::after{content:"";position:absolute;height:4px;width:16px;background:var(--cyan)}
.panel--diagnoses .heading::before{left:0;bottom:6px}
.panel--diagnoses .heading::after{right:0;top:6px}
.photo-grid{display:grid;grid-template-columns:repeat(3,1fr);gap:5px;margin:14px 0 14px}
.photo-grid .photo{height:58px;border-bottom:4px solid var(--navy)}
.diagnosis-list{list-style:none;color:var(--ink-blue);font-size:10.6px;line-height:1.36}
.diagnosis-list li{padding-left:9px;position:relative}
.diagnosis-list li::before{content:"•";position:absolute;left:0}

/* outside: contact */
.panel--contact{background:radial-gradient(circle at 40% 35%,#2449b8,var(--navy) 60%,var(--navy-deep));color:var(--white);text-align:center;padding-top:30px}
.panel--contact .heading{font-size:17px}
.consult-box{margin:14px 20px 0;border:1px solid rgba(255,255,255,.75);padding:44px 12px 20px;position:relative;font-family:"Montserrat",sans-serif;font-weight:700;font-size:14px;line-height:1.3}
.consult-box svg{position:absolute;top:-14px;left:50%;transform:translateX(-50%);background:var(--navy);padding:0 6px}
.contact-list{list-style:none;margin-top:22px;font-family:"Montserrat",sans-serif;font-weight:700;font-size:12.5px;line-height:1.35}
.contact-list li{margin-bottom:14px}
.contact-list .icon{display:block;margin:0 auto 5px;width:20px;height:20px}
.follow{font-size:9px;letter-spacing:1.5px;color:var(--cyan-soft);font-weight:700;margin-top:-2px}
.follow-dots{display:flex;gap:6px;justify-content:center;margin-top:6px}
.follow-dots span{width:14px;height:14px;border-radius:50%;background:var(--cyan)}

/* outside: cover */
.panel--cover{background:var(--white)}
.panel--cover .photo{position:absolute}
.cover-head{background:var(--navy);height:106px;color:var(--white);text-align:center;padding-top:22px}
.cover-head .heading{font-size:19px;line-height:1.15}
.cover-tag{color:var(--cyan-soft);font-size:12.5px;margin-top:6px;line-height:1.2}
.band{position:absolute;left:0;right:0;height:7px;background:var(--cyan)}
.cover-brand{position:absolute;top:440px;left:0;right:0;display:flex;align-items:center;justify-content:center;gap:8px}
.cover-brand .mark{width:22px;height:22px;background:var(--navy)}
.cover-brand .name{font-family:"Libre Baskerville",serif;color:var(--navy);font-size:21px}
.web-bar{position:absolute;left:20px;right:20px;top:500px;height:38px;border-radius:12px 12px 0 12px;background:var(--navy);color:var(--white);font-size:11px;letter-spacing:.6px;display:flex;align-items:center;justify-content:center;white-space:nowrap}

/* inside */
.panel--inside{background:var(--navy);display:flex;flex-direction:column}
.panel--inside .photo{flex:1 1 auto;min-height:0}
.ribbon{position:relative;z-index:1;margin:-18px 10px 0 0;flex:0 0 36px;height:36px;background:var(--white);clip-path:polygon(0 22%,100% 0,97% 100%,0 100%);color:var(--navy);font-size:15px;display:flex;align-items:flex-end;padding:0 0 6px 18px}
.text-box{flex:0 0 auto;background:var(--cyan);color:var(--white);font-size:10px;line-height:1.3;padding:10px 12px}
.text-box p+p{margin-top:7px}
.testimonial{flex:0 0 auto;position:relative;margin-top:10px;background:var(--white);padding:38px 12px 10px;text-align:center;color:#222;font-size:9.5px;line-height:1.32}
.testimonial .quote{position:absolute;left:10px;top:10px;width:24px;height:22px;background:var(--cyan);color:var(--white);font-family:"Montserrat",sans-serif;font-weight:800;font-size:20px;line-height:28px}
.testimonial .avatar{position:absolute;left:50%;top:6px;transform:translateX(-50%);width:26px;height:26px;border-radius:50%;background:linear-gradient(#b8c2cc,#6e7d8c)}
.testimonial .author{font-family:"Montserrat",sans-serif;font-weight:700;font-size:9.5px;letter-spacing:1px;margin-top:5px;color:#111}
.arrow-label{position:relative;flex:0 0 44px;height:44px;margin-top:14px}
.arrow-label svg{position:absolute;left:0;top:0}
.arrow-label span{position:absolute;left:16px;top:13px;font-size:14px;color:var(--navy)}
</style>
</head>
<body>

<section class="sheet sheet--outside" aria-label="Brochure outside">
  <div class="panel panel--diagnoses">
    <h2 class="heading">We treat a range<br>of diagnoses</h2>
    <div class="photo-grid">
      <div class="photo" role="img" aria-label="Child wearing a face mask"></div>
      <div class="photo" role="img" aria-label="Pelvic anatomy model"></div>
      <div class="photo" role="img" aria-label="Therapist treating a young patient"></div>
      <div class="photo" role="img" aria-label="Child wearing a face mask"></div>
      <div class="photo" role="img" aria-label="Pelvic anatomy model"></div>
      <div class="photo" role="img" aria-label="Therapist treating a young patient"></div>
    </div>
    <ul class="diagnosis-list">
      <li>Constipation</li>
      <li>Increased urinary frequency</li>
      <li>Decreased urinary frequency</li>
      <li>Day-time incontinence</li>
      <li>Night-time incontinence, bed-wetting, or enuresis</li>
      <li>Giggle incontinence</li>
      <li>Incontinence in the athletic female child or teenager</li>
      <li>Waking up in the night to urinate or nocturia</li>
      <li>Difficulty with urination: straining, slow flow, pain during or after urination</li>
      <li>Reduced sensation of bladder or bowel fullness</li>
      <li>Pain in the abdomen, bladder or lower back</li>
      <li>Fecal incontinence</li>
      <li>Treatment after pediatric pelvic Surgeries</li>
    </ul>
  </div>

  <div class="panel panel--contact">
    <h2 class="heading">Contact us</h2>
    <div class="consult-box">
      <svg width="40" height="30" viewBox="0 0 40 30" aria-hidden="true" fill="none" stroke="#fff" stroke-width="2.4" stroke-linecap="round">
        <circle cx="10" cy="5" r="3" fill="#fff"/><circle cx="30" cy="5" r="3" fill="#fff"/>
        <path d="M10 10v9h6v8M30 10v9h-6v8M15 15h10M6 12v15M34 12v15"/>
      </svg>
      We offer a FREE 15 minute consultation to help you determine if therapy is right for you
    </div>
    <ul class="contact-list">
      <li><svg class="icon" viewBox="0 0 20 20" aria-hidden="true"><circle cx="10" cy="10" r="10" fill="var(--cyan)"/><path d="M6.5 5.5l2 0 1 2.5-1.3 1a6 6 0 0 0 2.8 2.8l1-1.3 2.5 1v2a1 1 0 0 1-1 1A8.5 8.5 0 0 1 5.5 6.5a1 1 0 0 1 1-1z" fill="#fff"/></svg>555.014.2290</li>
      <li><svg class="icon" viewBox="0 0 20 20" aria-hidden="true"><circle cx="10" cy="10" r="10" fill="var(--cyan)"/><path d="M10 4.5a3.6 3.6 0 0 0-3.6 3.6c0 2.7 3.6 7 3.6 7s3.6-4.3 3.6-7A3.6 3.6 0 0 0 10 4.5z" fill="#fff"/><circle cx="10" cy="8.1" r="1.3" fill="var(--cyan)"/></svg>48 Harbor Lane<br>Ground Floor<br>Riverton, NY 10099</li>
      <li><svg class="icon" viewBox="0 0 20 20" aria-hidden="true"><circle cx="10" cy="10" r="10" fill="var(--cyan)"/><rect x="5" y="6.5" width="10" height="7" fill="#fff"/><path d="M5 6.5l5 4 5-4" stroke="var(--cyan)" fill="none"/></svg>contact@marlowcrestpt.example</li>
      <li><svg class="icon" viewBox="0 0 20 20" aria-hidden="true"><circle cx="10" cy="10" r="10" fill="var(--cyan)"/><path d="M6 5l9 4-4 1.3L9.5 15z" fill="#fff"/></svg>marlowcrestpt.example</li>
    </ul>
    <p class="follow">-FOLLOW US-</p>
    <div class="follow-dots" aria-hidden="true"><span></span><span></span><span></span><span></span></div>
  </div>

  <div class="panel panel--cover">
    <header class="cover-head">
      <h1 class="heading">Pediatric<br>Pelvic Health</h1>
      <p class="cover-tag">Treating infants, Children<br>&amp; Adolescents</p>
    </header>
    <div class="band" style="top:108px"></div>
    <div class="photo" style="top:118px;left:0;right:0;height:276px" role="img" aria-label="Smiling team of pediatric clinicians in white coats and scrubs"></div>
    <div class="band" style="top:394px"></div>
    <div class="cover-brand"><span class="mark"></span><span class="name">Marlow Crest</span></div>
    <div class="web-bar">MARLOWCRESTPT.EXAMPLE</div>
  </div>
</section>

<section class="sheet sheet--inside" aria-label="Brochure inside">
  <div class="panel panel--inside">
    <div class="photo" style="background:linear-gradient(135deg,#f3f5f7,#d9e6ee 60%,#bcd3e2)" role="img" aria-label="Clinician reviewing notes on a tablet"></div>
    <h2 class="heading ribbon">We help</h2>
    <div class="text-box">
      <p>Although millions of children suffer from pelvic floor dysfunction, it often takes a long time to receive the right treatment.</p>
      <p>Typically, children are toilet trained by age 4. After age 4, bowel and bladder dysfunction is considered a major medical issue that affects the family unit.</p>
      <p>Pelvic problems in children greatly influence the quality of life, self-image, social interactions, participation in sports, etc. A pelvic</p>
    </div>
    <div class="arrow-label">
      <svg width="214" height="44" viewBox="0 0 214 44" aria-hidden="true"><path d="M0 10H176V0L214 22 176 44V34H0z" fill="#fff"/></svg>
      <span class="heading">Testimonials</span>
    </div>
  </div>

  <div class="panel panel--inside">
    <div class="photo" style="background:linear-gradient(135deg,#dfe6ee,#7fa3c8 55%,#2f6fb5)" role="img" aria-label="Medical team reviewing an x-ray together"></div>
    <h2 class="heading ribbon">We specialize</h2>
    <div class="text-box">
      <p>All pelvic physical therapy treatments are always done with a physical therapist trained in pediatric pelvic floor issues, and always with your doctor's knowledge. Children are dressed and parents and guardians are present.</p>
      <p>During each session, your child or teen will work exclusively with one of our pelvic health physical therapists to help build strength, improve movement, and strengthen the skills and confidence needed to complete daily activities.</p>
    </div>
    <blockquote class="testimonial">
      <span class="quote">”</span><span class="avatar" role="img" aria-label="Reviewer portrait"></span>
      <p>Lorem ipsum dolor sit amet, consectetuer adipiscing elit, sed diam nonummy nibh euismod tincidunt ut laoreet dolore magna aliquam erat volutpat. Ut wisi enim ad minim veniam, quis nostrud exerci tation ullamcorper suscipit lobortis nisl ut aliquip ex ea commodo consequat. Duis autem vel eum iriure dolor in</p>
      <p class="author">ALEX MORGAN</p>
    </blockquote>
  </div>

  <div class="panel panel--inside">
    <div class="photo" style="background:linear-gradient(135deg,#cfe4f2,#9cc7e4 55%,#e8eef3)" role="img" aria-label="Care team meeting with a patient's family"></div>
    <h2 class="heading ribbon">We partner</h2>
    <div class="text-box">
      <p>Pelvic dysfunction problems in children in general, and in those with neurological pathologies even more, are markedly different from those in adults. Thus a therapist needs to work with parents, teachers, and other healthcare professionals such as urologists, GI's, pediatric physical therapists, and psychologists to provide an integrated and comprehensive plan of care.</p>
    </div>
    <blockquote class="testimonial">
      <span class="quote">”</span><span class="avatar" role="img" aria-label="Reviewer portrait"></span>
      <p>Lorem ipsum dolor sit amet, consectetuer adipiscing elit, sed diam nonummy nibh euismod tincidunt ut laoreet dolore magna aliquam erat volutpat. Ut wisi enim ad minim veniam, quis nostrud exerci tation ullamcorper suscipit lobortis nisl ut aliquip ex ea commodo consequat. Duis autem vel eum iriure dolor in hendrerit in vulputate velit esse molestie consequat, vel illum dolore eu feugiat nulla facilisis at vero eros et accumsan et iusto odio dignissim qui blandit praesent luptatum zzril</p>
      <p class="author">ALEX MORGAN</p>
    </blockquote>
  </div>
</section>

</body>
</html>
```